Restaurant needs a vertical banner for fried catfish

Our restaurant is looking for an eye-catching 78.75in. x 36in. vertical physical banner ad for our fried catfish. Photos for the fried catfish will be provided as a reference but we will also accept anything similar to the photo. We will be using the following as our receptacle: https://www.plankoria.example/banner-stand/retractable-banner-stands/
The design must incorporate the following flavor texts:
Fried Catfish
Always Fresh!
Made from Scratch
Hand-cut Fillets
The Best Catfish in Texas
Served with fries, hush puppies, and a 32oz fountain drink
Also available by the pound!
The final design should be creative, professional, and eye-catching for customers.
Updates
Colors
Designer to choose colors to be used in the design.
Requirements
Must have
- We are open to any and all design elements, albeit the 'flavor texts' should not overpower, but complement the fried catfish photo. 'Fried Catfish' can be used in lieu of a main title/logo.
Nice to have
- Transparent or textured backgrounds that can encompass any or all part of the banner such as a cutting board, shadows, abstract, etc to show depth are a plus.
- Use of vectors or objects such as ribbons or shapes to encapsulate the 'flavor texts' are also encouraged.

```html
<!DOCTYPE html>
<html lang="en">
<head>
<meta charset="utf-8">
<title>Fried Catfish Banner</title>
<link href="https://fonts.googleapis.com/css2?family=Josefin+Sans:wght@700&family=Montserrat:wght@600&family=Fira+Sans:ital,wght@1,600&display=swap" rel="stylesheet">
<style>
  :root {
    --cream: #fef9c6;
    --gold: #c9962d;
    --gold-shadow: #b89a4e;
    --bubble: #fed9a0;
    --bubble-text: #6b6257;
  }
  html, body { margin: 0; padding: 0; overflow: hidden; }
  body { width: 1200px; height: 2625px; background: var(--cream); }
  .banner { position: relative; width: 1200px; height: 2625px; background: var(--cream); overflow: hidden; }
  .hero { position: absolute; left: 0; top: 0; width: 1200px; height: 1000px; }
  .plate-photo {
    position: absolute; left: 57px; top: 875px; width: 560px; height: 560px;
    border-radius: 50%;
    background: radial-gradient(circle at 55% 55%, #d9a25a 0%, #c08642 45%, #7d5a3a 80%, #5c4330 100%);
    box-shadow: 0 8px 18px rgba(150, 120, 60, 0.45);
  }
  .bubble { position: absolute; left: 675px; top: 1225px; width: 446px; height: 305px; }
  .bubble-text {
    position: absolute; left: 675px; top: 1365px; width: 446px; margin: 0;
    text-align: center; font-family: 'Fira Sans', sans-serif; font-style: italic; font-weight: 600;
    font-size: 50px; line-height: 62px; color: var(--bubble-text);
  }
  .title {
    position: absolute; left: 54px; top: 1680px; margin: 0;
    font-family: 'Josefin Sans', sans-serif; font-weight: 700; font-size: 92px;
    letter-spacing: 2px; color: var(--gold); line-height: 1;
  }
  .features {
    position: absolute; left: 56px; top: 1880px; margin: 0; padding: 0; list-style: none;
    font-family: 'Montserrat', sans-serif; font-weight: 600; font-size: 48px; line-height: 62px;
    color: var(--gold);
  }
  .features li { margin-bottom: 60px; }
  .features li:last-child { margin-bottom: 0; }
</style>
</head>
<body>
  <div class="banner">
    <svg class="hero" viewBox="0 0 1200 1000" role="img" aria-label="Photo of golden fried catfish fillets on a plate with lettuce, one fillet dipped in a creamy sauce">
      <defs>
        <linearGradient id="heroFill" x1="0" y1="0" x2="1" y2="1">
          <stop offset="0" stop-color="#6d6a63"/>
          <stop offset="0.3" stop-color="#c2843d"/>
          <stop offset="0.65" stop-color="#b97a35"/>
          <stop offset="1" stop-color="#8fb33e"/>
        </linearGradient>
        <filter id="curveShadow" x="-5%" y="-5%" width="110%" height="120%">
          <feDropShadow dx="0" dy="8" stdDeviation="8" flood-color="#b89a4e" flood-opacity="0.55"/>
        </filter>
      </defs>
      <path filter="url(#curveShadow)" fill="url(#heroFill)"
        d="M0 0 H1200 V985 C1050 960 820 960 640 860 C450 760 330 640 190 560 C120 520 60 500 0 495 Z"/>
    </svg>

    <div class="plate-photo" role="img" aria-label="Photo of fried catfish bites on a white plate with a dipping sauce and lettuce"></div>

    <svg class="bubble" viewBox="0 0 446 305" aria-hidden="true">
      <path fill="var(--bubble)" d="M150 0 L245 70 H420 Q446 70 446 96 V279 Q446 305 420 305 H26 Q0 305 0 279 V96 Q0 70 26 70 H185 Z"/>
    </svg>
    <p class="bubble-text">The Best Catfish<br>in Texas</p>

    <h1 class="title">FRIED CATFISH</h1>

    <ul class="features">
      <li>Always Fresh</li>
      <li>Made From Scratch</li>
      <li>Hand Cut Fillets</li>
      <li>Served With Fries, Hush Puppies,<br>and a 32oz Fountain Drink</li>
      <li>Also Available by the Pound!</li>
    </ul>
  </div>
</body>
</html>
```